TKA Electricial Contracting Services

Hi guys, after a design for my small electrical company, have logo design files to be incorporated into the layout, the basic concept is electrical contracting services for residential, commercial, industrial & data services, image is clean clear and strong,

Card format is to have a nice clean logo on front,with maybe the Residential – commercial – industrial - data, followed with licensed & insured, followed by contact details on backside of the card.

Target Market(s)

Residential, commercial, industrial sectors.

Industry/Entity Type

Electrical

Contact Information for Business Card

TKA logo,
Residential – commercial – industrial - data
REC: 61372
Email: tka@poralink.net.au
Phone: 0458 203 719

Requirements
Must have
• Clean & strong design.
Nice to have
• If possible, I would like the logo colours inverted so the text is orange and the background is black on the front of the card, then the backside of the card be the reverse colour
Should not have
• No Sparks, lightning bolts,

```html
<!DOCTYPE html>
<html lang="en">
<head>
<meta charset="utf-8">
<title>TKA Electrical Business Card</title>
<link href="https://fonts.googleapis.com/css2?family=Saira:wght@600&family=Open+Sans:wght@400;700&display=swap" rel="stylesheet">
<style>
  :root {
    --orange: #f3842f;
    --black: #000000;
    --page: #ffffff;
  }
  html, body {
    margin: 0;
    padding: 0;
    width: 1200px;
    height: 1000px;
    overflow: hidden;
    background: var(--page);
  }
  .canvas {
    position: relative;
    width: 1200px;
    height: 1000px;
  }
  .card {
    position: absolute;
    left: 339px;
    width: 546px;
    height: 353px;
  }
  .card-front {
    top: 147px;
    background: var(--black);
  }
  .card-back {
    top: 510px;
    background: var(--orange);
  }
  .brand {
    position: absolute;
    left: 0;
    top: 0;
    width: 546px;
    height: 353px;
  }
  .brand text {
    font-family: "Saira", "Arial Narrow", sans-serif;
    font-weight: 600;
  }
  .brand-front text { fill: var(--orange); }
  .brand-back text { fill: var(--black); }
  .contact-list {
    position: absolute;
    left: 145px;
    top: 108px;
    margin: 0;
    padding: 0;
    list-style: none;
  }
  .contact-item {
    display: flex;
    align-items: center;
    height: 58px;
    font-family: "Open Sans", Arial, sans-serif;
    font-size: 20px;
    color: var(--black);
  }
  .contact-icon {
    width: 62px;
    height: 40px;
    margin-right: 12px;
    flex: none;
  }
  .licence-bar {
    position: absolute;
    left: 0;
    bottom: 0;
    width: 546px;
    height: 26px;
    background: var(--black);
    color: var(--orange);
    font-family: "Open Sans", Arial, sans-serif;
    font-weight: 700;
    font-size: 12px;
    line-height: 26px;
    padding-left: 18px;
    box-sizing: border-box;
  }
</style>
</head>
<body>
<div class="canvas">

  <section class="card card-front">
    <svg class="brand brand-front" viewBox="0 0 546 353" aria-label="Tyler Kane Electrical">
      <text x="101" y="218" font-size="176" textLength="370" lengthAdjust="spacingAndGlyphs">TKA</text>
      <text x="101" y="258" font-size="30" textLength="370" lengthAdjust="spacingAndGlyphs">Tyler Kane Electrical</text>
    </svg>
  </section>

  <section class="card card-back">
    <svg class="brand brand-back" viewBox="0 0 546 353" aria-label="Tyler Kane Electrical">
      <text x="351" y="68" font-size="74" textLength="158" lengthAdjust="spacingAndGlyphs">TKA</text>
      <text x="351" y="86" font-size="13" textLength="158" lengthAdjust="spacingAndGlyphs">Tyler Kane Electrical</text>
    </svg>

    <ul class="contact-list">
      <li class="contact-item">
        <svg class="contact-icon" viewBox="0 0 62 40" aria-hidden="true">
          <circle cx="24" cy="20" r="19" fill="none" stroke="var(--black)" stroke-width="5"/>
          <text x="24" y="27" text-anchor="middle" font-family="Open Sans, Arial, sans-serif" font-weight="700" font-size="19" fill="var(--black)">24</text>
        </svg>
        <span>Maintenance Service</span>
      </li>
      <li class="contact-item">
        <svg class="contact-icon" viewBox="0 0 62 40" aria-hidden="true">
          <path d="M2 12 Q29 -4 56 12 L56 18 L46 18 L44 11 Q29 6 14 11 L12 18 L2 18 Z" fill="var(--black)"/>
          <path d="M16 16 L42 16 L50 38 L8 38 Z" fill="var(--black)"/>
          <g fill="var(--orange)">
            <rect x="23" y="22" width="3" height="3"/><rect x="28" y="22" width="3" height="3"/><rect x="33" y="22" width="3" height="3"/>
            <rect x="23" y="27" width="3" height="3"/><rect x="28" y="27" width="3" height="3"/><rect x="33" y="27" width="3" height="3"/>
            <rect x="23" y="32" width="3" height="3"/><rect x="28" y="32" width="3" height="3"/><rect x="33" y="32" width="3" height="3"/>
          </g>
        </svg>
        <span>0458 203 719</span>
      </li>
      <li class="contact-item">
        <svg class="contact-icon" viewBox="0 0 62 40" aria-hidden="true">
          <rect x="0" y="4" width="60" height="34" fill="var(--black)"/>
          <path d="M2 6 L30 26 L58 6" fill="none" stroke="var(--orange)" stroke-width="2"/>
        </svg>
        <span>tka@poralink.net.au</span>
      </li>
    </ul>

    <div class="licence-bar">REC: 12345</div>
  </section>

</div>
</body>
</html>
```